Professional
Mark Elwood
President
4217 Vista Arroyo Place, NW
Albuquerque, NM 87114
melwood@emibq.com
www.emibq.com
New Construction*Remodels* Renovations*Handyman Services
Here is my logo for the stationary and business cards
Logo .AI file

```html
<!DOCTYPE html>
<html lang="en">
<head>
<meta charset="utf-8">
<title>Elwood Masonry, Inc — Business Card</title>
<link href="https://fonts.googleapis.com/css2?family=Montserrat:wght@500;700;800&family=Open+Sans:wght@400;600&display=swap" rel="stylesheet">
<style>
  :root {
    --bg: #e9e7e3;
    --card: #ffffff;
    --red: #d8232a;
    --ink: #2b2b2b;
    --grey: #6b6b6b;
    --rule: #d9d9d9;
    --black: #1a1a1a;
  }
  * { box-sizing: border-box; margin: 0; padding: 0; }
  html, body { width: 1200px; height: 646px; overflow: hidden; background: var(--bg); }
  .stage {
    width: 1200px; height: 646px;
    display: flex; align-items: center; justify-content: center; gap: 50px;
  }
  .card {
    position: relative;
    width: 525px; height: 300px;
    background: var(--card);
    box-shadow: 0 4px 14px rgba(0,0,0,.12);
    overflow: hidden;
    font-family: "Open Sans", Arial, sans-serif;
    color: var(--ink);
  }

  /* front */
  .front-brand {
    position: absolute; left: 0; right: 0; top: 70px;
    display: flex; align-items: center; justify-content: center; gap: 16px;
  }
  .brand-dot { width: 66px; height: 66px; border-radius: 50%; background: var(--red); flex: none; }
  .brand-name {
    font-family: "Montserrat", Arial, sans-serif; font-weight: 800;
    font-size: 30px; line-height: 1.05; color: var(--ink); letter-spacing: .5px;
  }
  .brand-name small { display: block; font-size: 30px; }
  .services { position: absolute; left: 0; right: 0; top: 178px; text-align: center; }
  .services-lead {
    font-family: "Montserrat", Arial, sans-serif; font-weight: 700;
    font-size: 14px; color: var(--red);
  }
  .services-list { margin-top: 6px; font-size: 13px; color: var(--ink); }
  .services-list span + span::before { content: "\2022"; color: var(--red); margin: 0 8px; }
  .front-band { position: absolute; left: 0; right: 0; bottom: 0; height: 16px; background: var(--red); }
  .front-band::before {
    content: ""; position: absolute; left: 0; right: 0; top: -6px; height: 3px; background: var(--rule);
  }

  /* back */
  .contact-name {
    position: absolute; left: 40px; top: 40px;
    font-family: "Montserrat", Arial, sans-serif; font-weight: 700; font-size: 22px; color: var(--red);
  }
  .contact-title { position: absolute; left: 40px; top: 72px; font-size: 13px; font-weight: 600; color: var(--grey); }
  .contact-address { position: absolute; left: 40px; top: 106px; font-size: 12.5px; line-height: 1.5; color: var(--ink); }
  .contact-list { position: absolute; left: 40px; top: 160px; list-style: none; font-size: 12.5px; }
  .contact-list li { display: flex; align-items: center; gap: 9px; height: 21px; }
  .contact-list svg { width: 14px; height: 14px; flex: none; }
  .back-band-black {
    position: absolute; right: 0; bottom: 0; width: 150px; height: 26px; background: var(--black);
    clip-path: polygon(22px 0, 100% 0, 100% 100%, 0 100%);
  }
  .back-band-red {
    position: absolute; left: 0; right: 150px; bottom: 0; height: 8px; background: var(--red);
  }
  .back-dot {
    position: absolute; right: 32px; bottom: 40px; width: 34px; height: 34px;
    border-radius: 50%; background: var(--red);
  }
</style>
</head>
<body>
<main class="stage">
  <section class="card card-front" aria-label="Card front">
    <div class="front-brand">
      <div class="brand-dot"></div>
      <div class="brand-name">ELWOOD<small>MASONRY, INC</small></div>
    </div>
    <div class="services">
      <p class="services-lead">New Construction</p>
      <p class="services-list"><span>Remodels</span><span>Renovations</span><span>Handyman Services</span></p>
    </div>
    <div class="front-band"></div>
  </section>

  <section class="card card-back" aria-label="Card back">
    <h1 class="contact-name">Mark Elwood</h1>
    <p class="contact-title">President</p>
    <p class="contact-address">4217 Vista Arroyo Place, NW<br>Albuquerque, NM 87114</p>
    <ul class="contact-list">
      <li><svg viewBox="0 0 14 14"><rect x="1" y="1" width="12" height="12" rx="2" fill="var(--red)"/><rect x="4" y="4" width="6" height="1.5" fill="#fff"/><rect x="4" y="7" width="6" height="1.5" fill="#fff"/></svg>License: 384017</li>
      <li><svg viewBox="0 0 14 14"><circle cx="7" cy="7" r="6.5" fill="var(--red)"/><path d="M4.5 3.5l1.5 0 .7 2-1 .8a5 5 0 0 0 2 2l.8-1 2 .7v1.5c-3.5.3-6.3-2.5-6-6z" fill="#fff"/></svg>505-555-0186</li>
      <li><svg viewBox="0 0 14 14"><circle cx="7" cy="7" r="6.5" fill="var(--red)"/><rect x="4.5" y="3" width="5" height="8" rx="1" fill="#fff"/></svg>505-555-0143</li>
      <li><svg viewBox="0 0 14 14"><circle cx="7" cy="7" r="6.5" fill="var(--red)"/><rect x="3.5" y="4.5" width="7" height="5" fill="#fff"/><path d="M3.5 4.5l3.5 3 3.5-3" stroke="var(--red)" fill="none"/></svg>melwood@emibq.com</li>
      <li><svg viewBox="0 0 14 14"><circle cx="7" cy="7" r="6.5" fill="var(--red)"/><circle cx="7" cy="7" r="3.5" fill="none" stroke="#fff"/><path d="M3.5 7h7M7 3.5v7" stroke="#fff"/></svg>www.emibq.com</li>
    </ul>
    <div class="back-dot"></div>
    <div class="back-band-red"></div>
    <div class="back-band-black"></div>
  </section>
</main>
</body>
</html>
```